■デザインへの要望
1)フライヤーのイメージとしては明るく女性的なイメージを希望します。
2)人物写真は使わないでください。
3)コーポレートロゴを右上に配置してください。
ロゴの改変(色の変更や比率の変更)はご遠慮ください。
4)会のロゴを配置してください。
位置はお任せしますが、サイズの変更はご遠慮ください。
※前回のフライヤーを素材と一緒にお付けしますのでご参考になさってください。

■素材
1)フライヤーを作成する際に必要なロゴ等の画像等は

```html
<!DOCTYPE html>
<html lang="ja">
<head>
<meta charset="utf-8">
<title>ランチョンセミナー15 これからの摂食嚥下障害看護に何が求められているか</title>
<link rel="stylesheet" href="https://fonts.googleapis.com/css2?family=Noto+Sans+JP:wght@400;500;700&family=Noto+Serif+JP:wght@500;700&display=swap">
<style>
  :root {
    --teal: #17868c;
    --teal-dark: #0f6d73;
    --magenta: #d3246d;
    --pink: #e2407f;
    --ink: #2b2b2b;
    --sub-ink: #555;
    --green: #4fae3b;
    --paper: #ffffff;
  }
  * { margin: 0; padding: 0; box-sizing: border-box; }
  html, body { width: 846px; height: 1200px; overflow: hidden; background: var(--paper); }
  body { font-family: "Noto Sans JP", sans-serif; color: var(--ink); }
  .flyer {
    position: relative; width: 846px; height: 1200px; overflow: hidden;
    background:
      radial-gradient(circle at 760px 60px, rgba(23,134,140,0.07) 0 160px, transparent 161px),
      radial-gradient(circle at 820px 260px, rgba(226,64,127,0.05) 0 120px, transparent 121px),
      var(--paper);
  }
  .society { position: absolute; left: 48px; top: 30px; display: flex; align-items: center; gap: 12px; }
  .society-mark { width: 40px; height: 40px; border-radius: 50%; background: var(--teal); }
  .society-name { font-size: 18px; font-weight: 500; color: var(--ink); }
  .sponsor-name {
    position: absolute; right: 48px; top: 36px; display: flex; align-items: center; gap: 10px;
    font-size: 30px; font-weight: 700; color: var(--green);
  }
  .sponsor-name .dot { width: 22px; height: 22px; border-radius: 50%; background: var(--green); }
  .seminar-no {
    position: absolute; left: 48px; top: 70px; display: flex; align-items: center; gap: 16px;
    font-size: 22px; font-weight: 700; color: var(--ink); line-height: 1.2;
  }
  .seminar-no::after { content: ""; width: 440px; height: 2px; background: var(--teal); }
  .title { font-family: "Noto Serif JP", serif; font-weight: 700; color: var(--teal); }
  .title span { position: absolute; left: 116px; display: block; line-height: 1.15; white-space: nowrap; }
  .title .l1 { top: 108px; font-size: 60px; }
  .title .l2 { top: 184px; font-size: 76px; }
  .title .l3 { top: 282px; font-size: 65px; }
  .subtitle { position: absolute; left: 118px; top: 370px; font-family: "Noto Serif JP", serif; font-size: 22px; font-weight: 500; line-height: 1.3; }
  .subtitle-en { position: absolute; left: 118px; top: 402px; font-family: "Noto Serif JP", serif; font-size: 24px; font-weight: 700; color: var(--ink); line-height: 1.3; white-space: nowrap; }
  .date { position: absolute; left: 118px; top: 440px; font-size: 60px; font-weight: 700; color: var(--magenta); letter-spacing: 1px; line-height: 1.2; }
  .date small { font-size: 40px; }
  .date .wd { display: inline-block; width: 50px; height: 50px; line-height: 46px; text-align: center; border: 3px solid var(--magenta); border-radius: 50%; font-size: 30px; vertical-align: 8px; margin-left: 4px; }
  .info { position: absolute; left: 118px; top: 512px; font-size: 24px; font-weight: 500; line-height: 1.35; }
  .info .room { display: block; padding-left: 100px; font-size: 20px; }
  .person { position: absolute; left: 56px; display: flex; gap: 22px; }
  .person.chair { top: 622px; }
  .person.speaker { top: 712px; }
  .role {
    flex: none; width: 64px; height: 64px; border-radius: 50%; background: var(--pink);
    color: #fff; font-size: 22px; font-weight: 700; display: flex; align-items: center; justify-content: center;
  }
  .name { font-size: 38px; font-weight: 700; color: var(--teal-dark); letter-spacing: 4px; line-height: 1.2; }
  .name small { font-size: 28px; letter-spacing: 1px; }
  .affil { font-size: 17px; color: var(--sub-ink); line-height: 1.5; margin-top: 4px; }
  .hosts {
    position: absolute; left: 50%; top: 1100px; transform: translateX(-50%);
    width: 560px; height: 84px; border: 1.5px solid var(--teal); padding: 6px 0; text-align: center;
    font-size: 16px; line-height: 1.45;
  }
  .hosts .label { font-size: 14px; display: block; }
</style>
</head>
<body>
<main class="flyer">
  <header>
    <div class="society"><span class="society-mark"></span><span class="society-name">第25回日本嚥下ケア研究学会学術大会</span></div>
    <div class="sponsor-name"><span class="dot"></span>ハーモニア</div>
    <p class="seminar-no">ランチョンセミナー15</p>
  </header>

  <h1 class="title">
    <span class="l1">これからの</span>
    <span class="l2">摂食嚥下障害看護に</span>
    <span class="l3">何が求められているか</span>
  </h1>
  <p class="subtitle">「機能低下予防」と「終末期care」</p>
  <p class="subtitle-en">What is required in the future for dysphagia nursing</p>

  <p class="date">2019<small>年</small>9<small>月</small>7<small>日</small><span class="wd">土</span></p>
  <p class="info">
    [時 間] 12:00～13:00<br>
    [会 場] 港みらいホール 中央コンベンションセンター
    <span class="room">第8会場 2F 中会議室 201</span>
  </p>

  <section class="person chair">
    <span class="role">座長</span>
    <div>
      <p class="name">緑川 早苗 <small>先生</small></p>
      <p class="affil">桜ヶ丘看護大学 名誉教授</p>
    </div>
  </section>
  <section class="person speaker">
    <span class="role">演者</span>
    <div>
      <p class="name">藤野 真理 <small>先生</small></p>
      <p class="affil">公益社団法人みなと県看護協会 認定看護師教育課程課程長<br>摂食・嚥下障害看護認定看護師教育課程 主任教員</p>
    </div>
  </section>

  <footer class="hosts">
    <span class="label">【共 催】</span>
    第25回日本嚥下ケア研究学会学術大会<br>ハーモニア株式会社
  </footer>
</main>
</body>
</html>
```